Design for Cedar Lark Homes real estate agency

Incorporate logo into new business cards. I need to include the Brindley Vance logo incorporated into Cedar Lark Homes on one side of the card (attached). On the other side I see just the icon with "Maren Quill" (attached) with "Grounded in Candor" either included as is or removed from logo and rather put as a tag line on the business card separate from the main logo. Contact information:

Maren Quill
Associate Broker
Cell: 730-418-5093
Email: marenquill@cedarlarkhomes.example
Web: www.cedarlarkhomes.example

Target Market(s)

Buyers, Sellers, Builders and Investors of homes and land

Industry/Entity Type

Real Estate Agent

Contact Information for Business Card

My client base tend to be higher end home buyers, sellers, builders and investors. I have been more and more in land and subdivisions for builders and investors. The card should not be cluttered. Clean and simple - yet with an air of exclusive/high end

Colors

Designer to choose colors to be used in the design.

Requirements
Must have
• Must have the logo on one side that has Brindley Vance logo incorporated. The side that has my contact information does not have to have the Brindley Vance logo incorporated.
• Must include "Grounded in Candor" tag line either within logo (as is) or removed from logo and included in another position on the side of the business card with contact information.
Should not have
• Should not have Brindley Vance logo incorporated into Cedar Lark Homes logo on both sides of business card. Would like the Cedar Lark Homes logo that has Brindley Logo only on the back side of card without contact information.

```html
<!DOCTYPE html>
<html lang="en">
<head>
<meta charset="utf-8">
<title>Maren Quill — Business Card</title>
<link rel="stylesheet" href="https://fonts.googleapis.com/css2?family=Cinzel:wght@400;500&family=Montserrat:wght@400&family=Open+Sans:wght@400;600&display=swap">
<style>
  :root {
    --backdrop: #1c1d1d;
    --card-white: #ffffff;
    --card-gold: #d1ad2e;
    --brown: #5a3a14;
    --brown-deep: #3f2a14;
    --gold: #c9a227;
    --gold-light: #ecdba4;
    --ink-grey: #5f5f5f;
  }
  * { margin: 0; padding: 0; box-sizing: border-box; }
  html, body { width: 1200px; height: 1200px; overflow: hidden; }
  body { background: var(--backdrop); position: relative; font-family: "Open Sans", sans-serif; }

  .card { position: absolute; width: 359px; height: 630px; }
  .card--front { left: 156px; top: 197px; background: var(--card-white); text-align: center; }
  .card--back { left: 706px; top: 406px; background: var(--card-gold); text-align: center; }

  .brand-mark {
    position: absolute; left: 0; right: 0; top: 52px;
    display: flex; align-items: center; justify-content: center; gap: 8px;
    font-family: "Cinzel", serif; font-weight: 500; font-size: 15px;
    color: var(--gold); letter-spacing: 1px;
  }
  .brand-mark__dot { width: 12px; height: 12px; border-radius: 50%; background: var(--brown); }

  .lockup-name {
    position: absolute; left: 0; right: 0; top: 142px;
    font-family: "Cinzel", serif; font-weight: 500; font-size: 30px;
    letter-spacing: 3px; color: var(--brown);
  }
  .lockup-tagline {
    position: absolute; left: 0; right: 0; top: 181px;
    font-family: "Montserrat", sans-serif; font-size: 9.5px;
    letter-spacing: 4.3px; color: var(--brown); padding-left: 4px;
  }

  .agent-name {
    position: absolute; left: 0; right: 0; top: 321px;
    font-family: "Cinzel", serif; font-weight: 500; font-size: 26px;
    letter-spacing: 2px; color: var(--brown);
  }
  .agent-role {
    position: absolute; left: 0; right: 0; top: 353px;
    font-size: 13px; color: var(--ink-grey);
  }
  .agent-rule {
    position: absolute; left: 158px; top: 381px; width: 44px; height: 2px; background: var(--gold);
  }

  .contact-icons {
    position: absolute; left: 0; right: 0; top: 525px;
    display: flex; justify-content: center; gap: 9px;
  }
  .contact-icons svg { width: 18px; height: 18px; }

  .contact-list {
    position: absolute; left: 0; right: 0; top: 553px;
    list-style: none; font-size: 13px; line-height: 20px; color: var(--ink-grey);
  }
  .contact-list strong { font-weight: 600; color: var(--brown-deep); }

  .back-mark {
    position: absolute; left: 0; right: 0; top: 170px;
    display: flex; flex-direction: column; align-items: center; gap: 18px;
    font-family: "Cinzel", serif; font-weight: 500; font-size: 28px;
    color: var(--brown-deep); letter-spacing: 1px;
  }
  .back-mark__dot { width: 76px; height: 76px; border-radius: 50%; background: #6e5330; }

  .back-tagline {
    position: absolute; left: 0; right: 0; top: 414px;
    font-size: 28px; color: var(--gold-light); letter-spacing: 0.5px;
  }
</style>
</head>
<body>
  <section class="card card--front" aria-label="Business card, contact side">
    <div class="brand-mark"><span class="brand-mark__dot"></span>Cedar Lark Homes</div>
    <div class="lockup-name">MAREN QUILL</div>
    <div class="lockup-tagline">GROUNDED IN CANDOR</div>

    <div class="agent-name">MAREN QUILL</div>
    <div class="agent-role">Associate Broker</div>
    <div class="agent-rule"></div>

    <div class="contact-icons">
      <svg viewBox="0 0 20 20" aria-label="Phone"><circle cx="10" cy="10" r="10" fill="var(--gold)"/><rect x="7" y="4.5" width="6" height="11" rx="1.2" fill="none" stroke="#fff" stroke-width="1.3"/></svg>
      <svg viewBox="0 0 20 20" aria-label="Email"><circle cx="10" cy="10" r="10" fill="var(--gold)"/><rect x="5" y="6.5" width="10" height="7" rx="1" fill="none" stroke="#fff" stroke-width="1.3"/><path d="M5.5 7l4.5 3.5L14.5 7" fill="none" stroke="#fff" stroke-width="1.3"/></svg>
      <svg viewBox="0 0 20 20" aria-label="Website"><circle cx="10" cy="10" r="10" fill="var(--gold)"/><circle cx="10" cy="10" r="5.5" fill="none" stroke="#fff" stroke-width="1.3"/><path d="M4.5 10h11M10 4.5c2.4 2.8 2.4 8.2 0 11M10 4.5c-2.4 2.8-2.4 8.2 0 11" fill="none" stroke="#fff" stroke-width="1.1"/></svg>
    </div>
    <ul class="contact-list">
      <li>730-418-5093</li>
      <li>marenquill@cedarlarkhomes.example</li>
      <li>www.<strong>cedarlarkhomes</strong>.example</li>
    </ul>
  </section>

  <section class="card card--back" aria-label="Business card, brand side">
    <div class="back-mark"><span class="back-mark__dot"></span>Cedar Lark Homes</div>
    <div class="back-tagline">GROUNDED IN CANDOR</div>
  </section>
</body>
</html>
```